Lantern Trails of Hollowmere Valley Tour Flyer

I need a one page flyer, one sided, full color. The main part of the flyer should be ONLY ONE of the attached photos. All text is included with SAMPLE/EXAMPLE sizing, but actual sizing and placement, and FONT are up to you. Font should be clear and legible, and one font should be used for all titles/larger text, and another for all small/paragraph text.

```html
<!DOCTYPE html>
<html lang="en">
<head>
<meta charset="utf-8">
<title>Lantern Trails of Hollowmere Valley Tour Flyer</title>
<link href="https://fonts.googleapis.com/css2?family=Crimson+Text:wght@400;700&family=Alegreya+Sans:ital,wght@0,400;1,400&display=swap" rel="stylesheet">
<style>
  :root {
    --ink-light: #ffffff;
    --ink-dark: #2f2f2f;
    --ink-body: #222222;
    --stage-deep: #141414;
    --stage-mid: #2e2e2e;
    --stage-glow: #4a4a4a;
    --paper: #ffffff;
  }
  * { margin: 0; padding: 0; box-sizing: border-box; }
  html, body { width: 927px; height: 1200px; overflow: hidden; background: var(--paper); }
  .flyer { position: relative; width: 927px; height: 1200px; background: var(--paper); }

  .hero {
    position: absolute; left: 0; top: 0; width: 927px; height: 818px;
    background: radial-gradient(ellipse 60% 70% at 72% 30%, var(--stage-glow) 0%, var(--stage-mid) 45%, var(--stage-deep) 100%);
  }
  .hero-photo {
    position: absolute; left: 430px; top: 90px; width: 497px; height: 728px;
    background: radial-gradient(ellipse 55% 60% at 55% 55%, #2a2a2c 0%, #1c1c1e 60%, rgba(20,20,20,0) 100%);
  }

  .hero-copy { position: absolute; left: 45px; top: 58px; width: 400px; color: var(--ink-light); }
  .tour-title {
    font-family: "Crimson Text", Georgia, serif; font-weight: 400;
    font-size: 42px; line-height: 48px;
  }
  .with-the {
    font-family: "Crimson Text", Georgia, serif; font-size: 19px; margin-top: 10px;
  }
  .act-name {
    font-family: "Crimson Text", Georgia, serif; font-weight: 700;
    font-size: 42px; line-height: 48px; margin-top: 6px;
  }
  .hero-blurb {
    font-family: "Alegreya Sans", Arial, sans-serif; font-style: italic;
    font-size: 20.5px; line-height: 32.5px; margin-top: 36px; width: 395px;
  }

  .tagline {
    position: absolute; left: 52px; top: 842px;
    font-family: "Crimson Text", Georgia, serif; font-weight: 400;
    font-size: 47px; line-height: 51px; color: var(--ink-dark);
  }
  .bio {
    position: absolute; left: 52px; top: 951px; width: 830px;
    font-family: "Alegreya Sans", Arial, sans-serif; font-style: italic;
    font-size: 12.6px; line-height: 27.5px; color: var(--ink-body);
  }
  .press { position: absolute; left: 52px; top: 1064px; color: var(--ink-body);
    font-family: "Alegreya Sans", Arial, sans-serif; font-size: 21px; line-height: 39px; }
  .press em { font-style: italic; }
</style>
</head>
<body>
<main class="flyer">
  <section class="hero" role="img" aria-label="Portrait photograph of the countertenor in a dark suit against a dark studio backdrop">
    <div class="hero-photo"></div>
  </section>

  <header class="hero-copy">
    <h1 class="tour-title">“Lantern Trails of Hollowmere Valley”</h1>
    <p class="with-the">with the</p>
    <h2 class="act-name">Corin Ashdale Trio</h2>
    <p class="hero-blurb">The world's most beloved melodies in ten languages featuring songs like "Morning Harbor", "Le Ciel Doré", "Luna Serena", "River Under Stars", and more! Original, arrangements by an Lumen-winning composer tap into the rare talent of countertenor, Corin Ashdale, and his soloist collaborators, an outstanding Westmere-trained concert pianist, and a wind soloist from the Riverton Philharmonic on oboe, English horn, flute, and clarinet.</p>
  </header>

  <h2 class="tagline">The World's Favorite Melodies<br>Like You've Never Heard Them Before!</h2>

  <p class="bio">Corin Ashdale has performed around the world from Halvern Hall, to Eastbrook's Marlow Hall using extraordinary vocal range, versatility, and a hilarious rapport with the audience, to entertain. A full time member of the Aurora-winning ensemble Silverbough, his voice can be heard on every major record label with a range of artists from Delia Vance to the Northgate Philharmonic.</p>

  <div class="press">
    <p><em>“Ashdale has Star Quality”</em> — Pinecrest Ledger</p>
    <p><em>"Performances of Great Vitality and Verve"</em> — Bayview Chronicle</p>
  </div>
</main>
</body>
</html>
```